Brisou Pour Over Coffee Filter Packaging Design

We are a brand new company starting to sell coffee related products. The coffee filter that we are about to sell will be copper color. We are working on the exact product picture, but a temporary one will be in uploaded files.We want the box to be simple, yet elegant and not too flashy. We prefer black, rose gold, white design, but are open to other designs. The uploaded files are just samples of what we like. "Brisou" means "owl" in French, we want an owl to be on the logo. Coffee related logo design is best, but we are open to other ideas. Size of this particular packaging is 14x14x12 cm

Target Market(s)

Online Retail

Industry/Entity Type

It Company

Logo Text

"Brisou Products" and "Brisou"

Other font styles liked:
• Your choice

Colors

Designer to choose colors to be used in the design.

Requirements
Must have
• Owl on the logo. Product description in a word file attached.
Nice to have
• Read product description

```html
<!DOCTYPE html>
<html lang="en">
<head>
<meta charset="utf-8">
<title>Brisou Pour Over Coffee Filter – Box Wrap</title>
<link href="https://fonts.googleapis.com/css2?family=Montserrat:wght@300;700;800&family=Tinos:wght@400;700&family=Oswald:wght@300;400&family=Caveat:wght@500&display=swap" rel="stylesheet">
<style>
  :root{
    --stage:#d8d8da;
    --paper:#f8f4ee;
    --splash:#efe4d3;
    --brown:#7a5141;
    --brown-dark:#4a3128;
    --rose:#d39a76;
    --ink:#3d2f29;
    --copper:#b86a35;
    --steel:#d9cfc8;
  }
  *{box-sizing:border-box;margin:0;padding:0}
  html,body{width:1200px;height:728px;overflow:hidden;background:var(--stage)}
  .wrap{position:absolute;left:20px;top:219px;width:1160px;height:290px;background:var(--paper);overflow:hidden;
    box-shadow:0 2px 8px rgba(0,0,0,.12)}
  .splash{position:absolute;border-radius:50%;
    background:radial-gradient(circle,var(--splash) 0%,rgba(239,228,211,.5) 45%,rgba(239,228,211,0) 72%)}
  .panel{position:absolute;top:0;height:290px;width:580px;overflow:hidden}
  .panel--back{left:0}
  .panel--front{left:580px;border-left:1px solid rgba(122,81,65,.08)}

  .brand{position:absolute;font-family:"Montserrat",sans-serif;font-weight:800;color:var(--brown);letter-spacing:.5px;line-height:1;white-space:nowrap}
  .title{position:absolute;text-align:right;font-family:"Montserrat",sans-serif;color:var(--brown);
    padding-right:8px;border-right:2px solid var(--rose);line-height:1.08}
  .title__light{font-weight:300;display:block}
  .title__bold{font-weight:700;display:block}

  .copy{position:absolute;left:30px;top:20px;width:140px;font-family:"Tinos",serif;color:var(--ink);font-size:4.5px;line-height:5.2px}
  .copy h3{font-size:6.4px;font-weight:700;letter-spacing:.3px;margin-bottom:3px}
  .copy p{margin-bottom:3px}
  .copy .tips{margin-top:5px}
  .thanks{float:right;width:32px;height:26px;margin:0 0 3px 6px;border-radius:4px;
    background:linear-gradient(135deg,#d7b9a5,#eadcd0)}
  .bulb{float:right;margin:0 6px 2px 8px}
  .steps{position:absolute;left:30px;top:198px;width:192px;padding-left:5px;border-left:1px solid var(--rose);
    font-family:"Montserrat",sans-serif;font-size:3.9px;line-height:4.6px;color:var(--ink)}
  .steps h4{font-size:5.4px;font-weight:700;margin-bottom:3px}
  .steps li{list-style:none;margin-bottom:3px;text-transform:uppercase;color:#7c6a60}

  .product{position:absolute;top:145px;width:230px;height:148px;border-radius:48% 48% 10% 10%/30% 30% 10% 10%;
    background:linear-gradient(180deg,var(--steel) 0%,#e6d5cc 35%,#d8b9a6 60%,var(--copper) 85%,#8d5a33 100%)}
  .beans{position:absolute;top:230px;width:120px;height:62px;border-radius:40% 40% 0 0;
    background:radial-gradient(ellipse at 60% 60%,#5a2e1f 0%,#6e3b27 40%,rgba(110,59,39,0) 75%)}
  .owl{position:absolute;left:8px;top:40px;width:104px;height:140px;border-radius:45% 45% 30% 30%;
    background:linear-gradient(160deg,#b08a5c,#7d5a3a 60%,#5a3e28)}
  .bubble{position:absolute;left:132px;top:44px;width:142px;height:62px;border:1px solid #b9a79c;border-radius:50%;
    font-family:"Caveat",cursive;color:var(--brown-dark);font-size:12.5px;line-height:13px;padding:8px 0 0 18px;background:rgba(255,255,255,.35)}

  .features{position:absolute;left:455px;top:108px;width:116px;font-family:"Oswald",sans-serif;font-weight:300;
    font-size:4.3px;line-height:5px;color:var(--ink)}
  .features li{list-style:none;display:flex;gap:6px;margin-bottom:6px}
  .features svg{flex:0 0 9px}
</style>
</head>
<body>
<div class="wrap">
  <div class="splash" style="left:360px;top:20px;width:320px;height:240px"></div>
  <div class="splash" style="left:840px;top:40px;width:300px;height:230px"></div>

  <section class="panel panel--back">
    <div class="copy">
      <h3>HELLO THERE!</h3>
      <div class="thanks" role="img" aria-label="Hand-lettered thank you note"></div>
      <p>Thank you for purchasing one of the Brisou products! We hope you enjoy it! Here at Brisou, we like our coffee fresh and hot and so we strive to share our experience with you! We have put together a few tips on how to make your coffee experience the best, so check it out!</p>
      <p>Word of Wisdom from the Brisou Team: A good cup of coffee shared with a friend is like capturing happiness in a cup! Share the liquid gold (coffee that is) with others!</p>
      <h3 class="tips">TIPS AND TRICKS:</h3>
      <svg class="bulb" width="16" height="18" viewBox="0 0 16 18" fill="none" stroke="#4a3128" stroke-width=".8">
        <circle cx="8" cy="7" r="4.5"/><path d="M6 12h4M6.5 14h3M8 0.5v1.5M1 7h1.5M13.5 7H15M3 2.5l1 1M13 2.5l-1 1"/>
      </svg>
      <p>To make the best cup of coffee, make sure your grind is not too coarse and not too fine; it has to be just right! We recommend a medium-coarse grind for the best results.</p>
      <p>The darker the roast of your coffee the more "spicy" and bitter it will taste. Light roasts retain more caffeine. The optimum water temperature is 195 to 205 degrees Fahrenheit. Bring water to a boil, then let it sit for about 30 seconds.</p>
      <p>Pre-infusion: this is a very important step when using a pour over coffee filter. Pour just enough water to soak through the grounds and wait a moment before brewing.</p>
      <p>Keep the spout of the kettle as close to the brew bed as possible and, after pre-infusion, pour softly in a circular pattern.</p>
    </div>
    <div class="steps">
      <h4>INSTRUCTIONS</h4>
      <ul>
        <li>1. Place filter on your favorite mug and fill with a desired amount of coffee. We recommend 2-3 tablespoons per cup.</li>
        <li>2. Pre-infuse your coffee by pouring just enough hot water to soak through the grounds. Wait for 30 seconds.</li>
        <li>3. Pour desired amount of water onto your pre-infused coffee in circular motion. Do not pour too much at once.</li>
        <li>4. It should take about three minutes for a 6 ounce cup of coffee to finish dripping.</li>
        <li>5. Sit back and enjoy your cup of coffee.</li>
      </ul>
    </div>
    <div class="brand" style="left:462px;top:28px;font-size:22px">BRISOU</div>
    <h2 class="title" style="right:24px;top:122px">
      <span class="title__light" style="font-size:18px">POUR OVER</span>
      <span class="title__bold" style="font-size:18px">COFFEE</span>
      <span class="title__bold" style="font-size:18px">FILTER</span>
    </h2>
    <div class="product" style="left:220px" role="img" aria-label="Copper and stainless steel pour over coffee filter"></div>
    <div class="beans" style="left:385px" role="img" aria-label="Scattered roasted coffee beans"></div>
  </section>

  <section class="panel panel--front">
    <div class="owl" role="img" aria-label="Illustrated owl perched on a branch holding a coffee cup"></div>
    <div class="bubble">Don't miss out.<br>Enjoy your Coffee<br>at its best</div>
    <div class="brand" style="left:318px;top:28px;font-size:22px">BRISOU</div>
    <div class="brand" style="left:28px;top:234px;font-size:22px">BRISOU</div>
    <h2 class="title" style="right:24px;top:22px">
      <span class="title__light" style="font-size:13px">POUR OVER</span>
      <span class="title__bold" style="font-size:13px">COFFEE</span>
      <span class="title__bold" style="font-size:13px">FILTER</span>
    </h2>
    <div class="product" style="left:214px" role="img" aria-label="Copper and stainless steel pour over coffee filter"></div>
    <div class="beans" style="left:388px" role="img" aria-label="Scattered roasted coffee beans"></div>
    <ul class="features">
      <li><svg width="9" height="8" viewBox="0 0 9 8" stroke="#4a3128" stroke-width=".8"><path d="M0 1.5h9M0 4h9M0 6.5h9"/></svg>The perfect alternative to disposable paper filters, which rob your coffee of essential oils and nutrients.</li>
      <li><svg width="9" height="8" viewBox="0 0 9 8" fill="none" stroke="#4a3128" stroke-width=".8"><rect x="1" y="1" width="5" height="6"/><path d="M6 2.5h1.5v2.5H6"/></svg>Designed to fit on most cups, mugs, thermoses, small pots, and even carafes.</li>
      <li><svg width="9" height="8" viewBox="0 0 9 8" fill="none" stroke="#4a3128" stroke-width=".8"><path d="M0 7l4-4 2 2 3-3M6.5 2H9v2.5"/></svg>Laser cut 18/10 stainless double filter ensures that no grounds end up in your cup.</li>
      <li><svg width="9" height="8" viewBox="0 0 9 8" fill="none" stroke="#4a3128" stroke-width=".8"><path d="M4.5 0.5C3 3 2 4.3 2 5.3a2.5 2.5 0 005 0c0-1-1-2.3-2.5-4.8z"/></svg>Our pour over coffee filter does not absorb essential oils from coffee beans, allowing you to make a perfectly clean and flavorful coffee every single time.</li>
      <li><svg width="9" height="8" viewBox="0 0 9 8" fill="none" stroke="#4a3128" stroke-width=".8"><path d="M0.5 4C2 2 3.5 1.5 4.5 1.5S7 2 8.5 4C7 6 5.5 6.5 4.5 6.5S2 6 .5 4z"/><circle cx="4.5" cy="4" r="1.2"/></svg>Reusable and easy to clean - simply rinse well with warm water or throw it into the dishwasher.</li>
    </ul>
  </section>
</div>
</body>
</html>
```